Wix Web design for a Residential redevelopment company

I need a website with a modern and elegant feel that will attract investors. I would like for the color scale to include the colors in our logo and also shades of grey for a modern feel. I need a page for property case studies in which each case study includes property before and after photos, an imbeded youtube video and text in the format of a math problem showing the amount the property was bought for -(minus) what the investor got in return -(minus) rehab costs -(minus) taxes and fees =(equals) Net Profit
However instead of there being an equal sign, I want the math problem to go vertically down with an underline for the equals sign.There needs to be an "About us," page, Investor Inquiries page, Contact Us Page, and Case studies page.
For font formatting, we like Corporate Gothic. Please make the website Wix friendly.

When someone clicks on one of the case study pictures, I would like the pictures to pull up in a click or swipe to the right manner similar to how pictures are structured on mebrank or pendosa.com

Target Market(s)

Investors

Industry/Entity Type

Real Estate

Number of Pages Required

5+ page

Font styles to use
Other font styles liked:
• Gothic Corporate

Requirements
Nice to have
• stock photos for the home page

```html
<!DOCTYPE html>
<html lang="en">
<head>
<meta charset="utf-8">
<title>Maecenas Finibus – Case Study – Brixel Property Solutions</title>
<link rel="stylesheet" href="https://fonts.googleapis.com/css2?family=Montserrat:wght@500;600;700;800&family=Didact+Gothic&display=swap">
<style>
:root{
  --green:#74b941;
  --green-dark:#3e9a22;
  --green-deep:#2f7f18;
  --blue:#0b6fcb;
  --ink:#1d1d1d;
  --text:#3a3a3a;
  --grey-light:#f3f3f3;
  --footer:#1a1a1a;
  --footer-text:#b9b9b9;
  --white:#ffffff;
}
*{box-sizing:border-box;margin:0;padding:0}
html,body{width:1200px;height:2459px;overflow:hidden;background:var(--white)}
body{position:relative;font-family:"Didact Gothic",sans-serif;color:var(--text)}
.abs{position:absolute}

/* header */
.topbar{left:0;top:0;width:1200px;height:36px;background:linear-gradient(180deg,var(--green-deep),var(--green-dark))}
.topbar .contact{top:10px;font-size:11px;color:var(--white);display:flex;align-items:center;gap:7px}
.topbar .btn{top:8px;height:21px;border:1px solid var(--white);color:var(--white);font-size:10px;display:flex;align-items:center;justify-content:center}
.topbar .btn.solid{background:var(--white);color:var(--green-dark)}
.navband{left:0;top:36px;width:1200px;height:76px;background:var(--green)}
.nav a{position:absolute;top:30px;color:var(--white);font-family:"Montserrat",sans-serif;font-size:12px;font-weight:500;text-decoration:none}
.brand{left:161px;top:0;width:127px;height:131px;background:var(--white);clip-path:polygon(0 0,100% 0,100% 88%,50% 100%,0 88%);display:flex;flex-direction:column;align-items:center;justify-content:center;gap:8px;box-shadow:0 2px 6px rgba(0,0,0,.2)}
.brand .mark{width:26px;height:26px;border-radius:50%;background:var(--green)}
.brand .name{font-family:"Montserrat",sans-serif;font-weight:700;font-size:13px;color:var(--green-dark);text-align:center;line-height:15px}
.hero{left:0;top:112px;width:1200px;height:98px;background:linear-gradient(90deg,#5c5e63,#8d8a86 45%,#b9a99a 70%,#6e6f72)}
.hero::after{content:"";position:absolute;inset:0;background:rgba(20,20,20,.45)}
.hero h1{position:absolute;left:161px;top:34px;z-index:1;font-family:"Montserrat",sans-serif;font-weight:800;font-size:29px;color:var(--white);letter-spacing:.3px}
.crumbs{position:absolute;right:161px;top:51px;z-index:1;font-size:11px;color:var(--white);display:flex;gap:12px}

/* main */
h2.section{font-family:"Montserrat",sans-serif;font-weight:700;font-size:17px;color:var(--ink)}
.key-sub{left:161px;top:287px;border-left:7px solid var(--green);padding-left:22px;height:58px}
.key-sub h3{font-family:"Montserrat",sans-serif;font-size:14px;font-weight:700;color:var(--green-dark)}
.key-sub p{font-size:14px;color:var(--ink);line-height:19px;margin-top:5px}
.facts{left:161px;top:364px;font-size:12px;color:var(--ink);line-height:19px}
.facts b{font-family:"Montserrat",sans-serif;font-weight:700;font-size:12.5px}
.para{left:161px;width:654px;font-size:10.6px;line-height:17.6px;text-align:justify;color:var(--text)}
.media{left:161px;width:654px;height:252px;overflow:hidden}
.media .shade{position:absolute;inset:0;background:rgba(30,30,40,.35)}
.play{position:absolute;left:50%;width:44px;height:44px;margin-left:-22px;border:3px solid var(--white);border-radius:50%}
.play::after{content:"";position:absolute;left:15px;top:10px;border-left:15px solid var(--white);border-top:9px solid transparent;border-bottom:9px solid transparent}
.media .label{position:absolute;width:100%;top:78px;text-align:center;font-family:"Montserrat",sans-serif;font-weight:800;font-size:29px;color:var(--white)}
.arrow{position:absolute;top:98px;width:22px;height:56px;background:var(--green);display:flex;align-items:center;justify-content:center}

/* sidebar */
.download{left:836px;top:251px;width:203px;height:137px;background:var(--blue);text-align:center;color:var(--white)}
.download h4{font-family:"Montserrat",sans-serif;font-weight:700;font-size:15px;line-height:20px;margin-top:22px}
.download .pill{display:inline-block;margin-top:15px;width:142px;height:36px;border-radius:18px;background:var(--white);color:var(--blue);font-family:"Montserrat",sans-serif;font-weight:700;font-size:11px;line-height:36px}
.map-title{left:836px;top:413px;font-family:"Montserrat",sans-serif;font-weight:700;font-size:12.5px;color:var(--ink)}
.map{left:836px;top:439px;width:203px;height:176px;background:linear-gradient(160deg,#ececec,#dfe3dc);border:1px solid #d5d5d5}

/* related */
.card{top:1858px;width:203px}
.card .thumb{width:203px;height:120px;background:linear-gradient(180deg,#c8c3bd,#7e6a4f 55%,#8ba165)}
.card h5{margin-top:12px;font-family:"Didact Gothic",sans-serif;font-size:15px;font-weight:400;color:var(--ink)}
.card p{margin-top:5px;font-size:10.6px;line-height:17px;color:var(--ink)}

/* footer */
.footer{left:0;top:2087px;width:1200px;height:372px;background:var(--footer)}
.fcol{top:2137px;width:200px}
.fcol h6{font-family:"Montserrat",sans-serif;font-weight:700;font-size:12px;color:var(--white);margin-bottom:18px}
.fcol li{list-style:none;font-size:10.5px;color:var(--footer-text);line-height:24px}
.fcol li.more{color:var(--green)}
.fnav{top:2330px;left:0;width:1200px;display:flex;justify-content:center;gap:36px;font-size:10.5px;color:var(--footer-text)}
.frule{left:161px;top:2354px;width:878px;height:1px;background:#333}
.social{top:2378px;left:0;width:1200px;display:flex;justify-content:center;gap:14px}
.social span{width:34px;height:34px;border:2px solid #888;border-radius:50%}
.copy{top:2428px;left:0;width:1200px;text-align:center;font-size:10px;color:var(--footer-text)}
</style>
</head>
<body>

<header>
  <div class="abs topbar">
    <div class="abs contact" style="left:306px">
      <svg width="12" height="12" viewBox="0 0 24 24"><path fill="#fff" d="M6.6 10.8a15 15 0 0 0 6.6 6.6l2.2-2.2a1 1 0 0 1 1-.25 11.4 11.4 0 0 0 3.6.6 1 1 0 0 1 1 1V20a1 1 0 0 1-1 1A17 17 0 0 1 3 4a1 1 0 0 1 1-1h3.5a1 1 0 0 1 1 1c0 1.25.2 2.45.6 3.6a1 1 0 0 1-.25 1z"/></svg>
      +1 (555) 01234-5678
    </div>
    <div class="abs contact" style="left:440px">
      <svg width="14" height="11" viewBox="0 0 24 18"><rect x="1" y="1" width="22" height="16" fill="none" stroke="#fff" stroke-width="2"/><path d="M1 1l11 9 11-9" fill="none" stroke="#fff" stroke-width="2"/></svg>
      info@brixelproperty.com
    </div>
    <div class="abs btn" style="left:939px;width:40px">Log In</div>
    <div class="abs btn solid" style="left:991px;width:46px">Sign Up</div>
  </div>
  <nav class="abs navband nav">
    <a style="left:575px">Home</a>
    <a style="left:647px">About Us</a>
    <a style="left:734px">Investor Inquiries</a>
    <a style="left:872px">Case Studies</a>
    <a style="left:978px">Contact Us</a>
  </nav>
  <div class="abs hero" role="img" aria-label="Modern apartment buildings at sunset">
    <h1>MAECENAS FINIBUS</h1>
    <div class="crumbs"><span>HOME</span><span>›</span><span>CASE STUDIES</span><span>›</span><span>Maecenas Finibus</span></div>
  </div>
  <div class="abs brand">
    <span class="mark"></span>
    <span class="name">BRIXEL<br>Property Solutions</span>
  </div>
</header>

<main>
  <h2 class="abs section" style="left:161px;top:247px">KEY INFORMATION</h2>
  <div class="abs key-sub">
    <h3>MAECENAS FINIBUS</h3>
    <p>30500-30600 Fusce mollis massa nisl,<br>vitae scelerisque erat pulvinar eu.</p>
  </div>
  <div class="abs facts" style="left:161px"><b>PROPERTY TYPE</b><br><b>YEAR RENOVATED</b><br><b>SIZE</b></div>
  <div class="abs facts" style="left:324px">OFFICE<br>2008<br>±150,000</div>
  <div class="abs facts" style="left:407px;font-size:10.5px"><b>ASSIGNMENT TYPE</b><br>FACILITY MANAGEMENT,<br>PROPERTY &amp; ASSET MANAGEMENT</div>

  <p class="abs para" style="top:437px">Sed quis sagittis nisl. Maecenas finibus tempor nibh quis suscipit. Nunc suscipit purus id felis facilisis, sed auctor felis placerat. Pellentesque a tempor metus. Nullam nec diam consequat tortor porttitor feugiat et in nisl. Morbi mauris ex, mattis non luctus id, pulvinar nec ligula. Donec eu cursus risus. Sed a mi porta, faucibus sapien nec, laoreet lectus. In id rhoncus est. Morbi rutrum, sem vitae imperdiet aliquam, erat libero aliquam velit, vitae lobortis lacus enim eget mi. Duis urna tortor, tincidunt sed mi at, rutrum dapibus lectus. Pellentesque ac ante fringilla, congue tellus interdum, condimentum neque. Aenean euismod vitae turpis sed maximus. Aliquam sagittis finibus cursus.</p>

  <div class="abs media" style="top:567px;background:linear-gradient(180deg,#9a8f86,#6d6a63 45%,#4f5a3a)" role="img" aria-label="Case study video: modern apartment complex">
    <div class="shade"></div>
    <div class="label">CASE STUDY</div>
    <div class="play" style="top:121px"></div>
  </div>

  <p class="abs para" style="top:839px">Lorem ipsum dolor sit amet, consectetur adipiscing elit. Morbi et blandit purus, quis tristique sapien. Sed finibus efficitur libero, nec scelerisque dolor pretium quis. Fusce mollis massa nisl, vitae scelerisque erat pulvinar eu. Donec placerat lobortis congue. Nunc luctus, mi vitae ornare tempus, justo quam maximus orci, et mollis dolor dui eget quam. Pellentesque maximus interdum purus, molestie suscipit ante posuere at. Vivamus nec sodales purus. Phasellus malesuada, risus vitae ultricies lacinia, libero ex gravida sapien, in interdum lorem mi at nisi. In sed dapibus sapien, at elementum justo. Donec commodo vel tortor et malesuada. Suspendisse congue lobortis nisl id laoreet. Phasellus et leo purus. Nulla pulvinar quam a mi finibus, quis volutpat lorem consequat. Nunc sed libero vel lorem suscipit gravida. Quisque fringilla libero ac metus ultrices pharetra quis a ipsum. Maecenas at maximus metus, ac laoreet mi.</p>

  <div class="abs media" style="top:1003px;background:linear-gradient(180deg,#d9c2a4,#b59a78 35%,#6f6a5a 65%,#5e7a3c)" role="img" aria-label="Photo gallery: apartment buildings with landscaped garden">
    <div class="arrow" style="left:0"><svg width="8" height="12" viewBox="0 0 8 12"><path d="M7 1L2 6l5 5" fill="none" stroke="#fff" stroke-width="2"/></svg></div>
    <div class="arrow" style="right:0"><svg width="8" height="12" viewBox="0 0 8 12"><path d="M1 1l5 5-5 5" fill="none" stroke="#fff" stroke-width="2"/></svg></div>
  </div>

  <p class="abs para" style="top:1275px">Aenean nibh dui, imperdiet ac cursus vitae, sollicitudin eu enim. Donec eu lectus sed mauris sollicitudin suscipit a a mi. Cras mattis quis augue vel rhoncus. Proin vestibulum commodo nibh, vel consequat eros hendrerit a. Mauris eget est egestas, tincidunt elit eu, vehicula dui. Sed turpis lorem, lobortis in rutrum in, ornare vel libero. Suspendisse aliquet est ex, ut faucibus lectus tristique vitae. Ut sagittis, ex ut varius volutpat, neque urna tristique est, sit amet consectetur dui felis nec orci. In suscipit nunc ut mi euismod, in viverra velit fringilla. Quisque sed elementum elit. Donec rhoncus vestibulum lectus, eget rhoncus orci elementum non. Phasellus elementum vehicula vehicula. Quisque in enim ligula. Mauris scelerisque mattis elit at finibus.</p>

  <div class="abs media" style="top:1406px;background:linear-gradient(120deg,#8a8580,#a89d92 40%,#cfc6bb 70%,#7f8a70)" role="img" aria-label="Video: investors reviewing documents together">
    <div class="shade" style="background:rgba(30,30,40,.2)"></div>
    <div class="play" style="top:100px"></div>
  </div>

  <p class="abs para" style="top:1675px">Aenean nibh dui, imperdiet ac cursus vitae, sollicitudin eu enim. Donec eu lectus sed mauris sollicitudin suscipit a a mi. Cras mattis quis augue vel rhoncus. Proin vestibulum commodo nibh, vel consequat eros hendrerit a. Mauris eget est egestas, tincidunt elit eu, vehicula dui. Sed turpis lorem, lobortis in rutrum in, ornare vel libero. Suspendisse aliquet est ex, ut faucibus lectus tristique vitae. Ut sagittis, ex ut varius volutpat, neque urna tristique est, sit amet consectetur dui felis nec orci. In suscipit nunc ut mi euismod, in viverra velit fringilla. Quisque sed elementum elit. Donec rhoncus vestibulum lectus, eget rhoncus orci elementum non. Phasellus elementum vehicula vehicula. Quisque in enim ligula. Mauris scelerisque mattis elit at finibus.</p>

  <aside>
    <div class="abs download">
      <h4>Download the<br>Case Study</h4>
      <span class="pill">DOWNLOAD</span>
    </div>
    <div class="abs map-title">PROPERTY MAP</div>
    <div class="abs map" role="img" aria-label="Map showing the property location"></div>
  </aside>

  <h2 class="abs section" style="left:161px;top:1817px">RELATED CASE STUDIES</h2>
  <div class="abs card" style="left:161px"><div class="thumb" role="img" aria-label="Apartment building"></div><h5>Maecenas Finibus</h5><p>Lorem ipsum dolor sit amet, consectetur adipiscing elit. Morbi et blandit purus.</p></div>
  <div class="abs card" style="left:387px"><div class="thumb" role="img" aria-label="Apartment building"></div><h5>Maecenas Finibus</h5><p>Lorem ipsum dolor sit amet, consectetur adipiscing elit. Morbi et blandit purus.</p></div>
  <div class="abs card" style="left:611px"><div class="thumb" role="img" aria-label="Apartment building"></div><h5>Maecenas Finibus</h5><p>Lorem ipsum dolor sit amet, consectetur adipiscing elit. Morbi et blandit purus.</p></div>
  <div class="abs card" style="left:836px"><div class="thumb" role="img" aria-label="Apartment building"></div><h5>Maecenas Finibus</h5><p>Lorem ipsum dolor sit amet, consectetur adipiscing elit. Morbi et blandit purus.</p></div>
</main>

<footer>
  <div class="abs footer"></div>
  <div class="abs fcol" style="left:161px"><h6>REAL ESTATE MARKETS</h6><ul><li>Alabama Real Estate</li><li>Alaska Real Estate</li><li>Arizona Real Estate</li><li>Arkansas Real Estate</li><li class="more">More</li></ul></div>
  <div class="abs fcol" style="left:387px"><h6>RENTAL MARKETS</h6><ul><li>Alabama Rentals</li><li>Alaska Rentals</li><li>Arizona Rentals</li><li>Arkansas Rentals</li><li class="more">More</li></ul></div>
  <div class="abs fcol" style="left:611px"><h6>BROWSE HOMES</h6><ul><li>California</li><li>Texas</li><li>New York</li><li>Florida</li><li class="more">More</li></ul></div>
  <div class="abs fcol" style="left:836px"><h6>FOR PROFESSIONALS</h6><ul><li>Stats &amp; Trends</li><li>Home Price Maps</li><li>U.S. Property Records</li><li>Popular Counties</li><li class="more">More</li></ul></div>
  <div class="abs fnav"><span>Home</span><span>About Us</span><span>Investor Inquiries</span><span>Case Studies</span><span>Contact Us</span></div>
  <div class="abs frule"></div>
  <div class="abs social"><span></span><span></span><span></span><span></span></div>
  <div class="abs copy">Copyright © 2018 Brixel Property Solutions. All rights reserved.</div>
</footer>

</body>
</html>
```